K & D A/C Compressors' Business Card

Hello,

I need someone to create a new business card for my business. The name of my Business is: K & D A/C Compressors. I sell automotive air conditioning parts (a/c parts). I would like the business card to incorporate my logo, and to have an automotive feel to it. It is important that the business card feel like it is coming from an automotive parts business.

I already have a logo, which I will provide.

Thanks.
Updates

Project Deadline Extended Reason: I feel like extending the deadline until October 9, 2017, will allow for more time to design the business card. Thank you for your understanding. Added Monday, October 2, 2017

Target Market(s)

Consumers who need automotive a/c parts, and auto mechanics.

Industry/Entity Type

Automotive

Contact Information for Business Card

Business name: K & D A/C Compressors
Business Address: 48207 Southwest 36th Street, North Miami Beach, Florida 33162
Telephone: 305-472-1390
Fax: To be provided once I choose your design.
Website: www.kdcoolunits.example
Email: support@kdcoolunits.example
Names: To be provided once I choose your design.

Font styles to use
Sans Serif

Colors

Designer to choose colors to be used in the design.

Requirements
Must have
• The business card must include all of the "Business Card Details" and the logo I have uploaded.

```html
<!DOCTYPE html>
<html lang="en">
<head>
<meta charset="utf-8">
<title>K &amp; D A/C Compressors – Business Card</title>
<link href="https://fonts.googleapis.com/css2?family=Crimson+Text:wght@400;600&display=swap" rel="stylesheet">
<style>
  :root{
    --page:#e9e9e7;
    --card-black:#050505;
    --card-white:#ffffff;
    --accent:#2a9ad8;
    --ink:#1d1d1d;
    --muted:#bdbdbd;
    --shadow:rgba(0,0,0,.22);
  }
  *{margin:0;padding:0;box-sizing:border-box}
  html,body{width:1200px;height:1000px;overflow:hidden;background:var(--page)}
  body{position:relative;font-family:"Crimson Text",Georgia,serif}
  .card{position:absolute;left:200px;width:800px;height:457px;overflow:hidden;box-shadow:0 8px 24px var(--shadow)}
  .card--front{top:30px;background:var(--card-black)}
  .card--back{top:513px;background:var(--card-black)}

  /* front */
  .front__photo{position:absolute;left:0;top:0;width:800px;height:350px;
    background:linear-gradient(135deg,#2b2d30 0%,#14161a 45%,#3a3c40 70%,#101114 100%)}
  .front__rule{position:absolute;left:0;top:352px;width:800px;height:4px;background:var(--card-white)}
  .front__band{position:absolute;left:0;top:356px;width:800px;height:101px;display:flex;align-items:center;justify-content:space-between;padding:0 34px}
  .front__address{color:var(--muted);font-size:21px;line-height:1.25;text-align:right}

  /* brand name */
  .brand{display:flex;align-items:center;gap:12px;color:var(--card-white)}
  .brand__mark{width:18px;height:18px;background:var(--accent)}
  .brand__name{font-size:22px;font-weight:600;line-height:1.05;color:var(--card-white)}

  /* back */
  .back__art{position:absolute;inset:0}
  .back__brand{position:absolute;left:40px;top:236px}
  .back__info{position:absolute;right:58px;top:70px;width:420px;text-align:right;color:var(--ink)}
  .person__name{color:var(--accent);font-size:36px;font-weight:400;letter-spacing:.5px;line-height:1}
  .person__title{font-size:22px;margin-top:6px;padding-right:14px}
  .person__rule{height:2px;background:var(--accent);width:240px;margin:6px 0 0 auto}
  .back__address{font-size:20px;line-height:1.3;margin-top:46px}
  .contacts{list-style:none;margin-top:26px}
  .contact{display:flex;justify-content:flex-end;align-items:center;gap:14px;font-size:19px;letter-spacing:.6px;height:34px}
  .contact svg{width:18px;height:18px;fill:none;stroke:var(--accent);stroke-width:2}
  .contact svg .solid{fill:var(--accent);stroke:none}
</style>
</head>
<body>

<section class="card card--front">
  <div class="front__photo" role="img" aria-label="Photo of a car dashboard centre console with climate controls and gear lever"></div>
  <div class="front__rule"></div>
  <div class="front__band">
    <div class="brand">
      <span class="brand__mark"></span>
      <span class="brand__name">K &amp; D<br>A/C Compressors</span>
    </div>
    <p class="front__address">48207 Southwest 36th Street,<br>Harbor Bay, Florida 34990</p>
  </div>
</section>

<section class="card card--back">
  <svg class="back__art" viewBox="0 0 800 457" aria-hidden="true">
    <polygon points="405,0 800,0 800,457 385,457 280,228" fill="var(--accent)"/>
    <polygon points="425,0 800,0 800,457 405,457 300,228" fill="var(--card-white)"/>
  </svg>

  <div class="back__brand brand">
    <span class="brand__mark"></span>
    <span class="brand__name">K &amp; D<br>A/C Compressors</span>
  </div>

  <div class="back__info">
    <h1 class="person__name">DANA REYES</h1>
    <p class="person__title">General Manager</p>
    <div class="person__rule"></div>
    <p class="back__address">48207 Southwest 36th Street,<br>Harbor Bay, Florida 34990</p>
    <ul class="contacts">
      <li class="contact"><span>305 472 1390</span>
        <svg viewBox="0 0 20 20"><path class="solid" d="M4 2l3 0 2 4-2 2c1 2 3 4 5 5l2-2 4 2v3c0 1-1 2-2 2C9 18 2 11 2 4c0-1 1-2 2-2z"/></svg></li>
      <li class="contact"><span>305 472 1391</span>
        <svg viewBox="0 0 20 20"><rect class="solid" x="5" y="2" width="10" height="5"/><rect class="solid" x="2" y="7" width="16" height="7" rx="1"/><rect x="6" y="12" width="8" height="6"/></svg></li>
      <li class="contact"><span>support@kdcoolunits.example</span>
        <svg viewBox="0 0 20 20"><rect x="2" y="4" width="16" height="12"/><path d="M2 4l8 7 8-7M2 16l6-6M18 16l-6-6"/></svg></li>
      <li class="contact"><span>www.kdcoolunits.example</span>
        <svg viewBox="0 0 20 20"><circle cx="10" cy="10" r="8"/><ellipse cx="10" cy="10" rx="3.5" ry="8"/><path d="M2 10h16M4 5.5h12M4 14.5h12"/></svg></li>
    </ul>
  </div>
</section>

</body>
</html>
```